Business Card for Voltrix

Horizontal business card for voltrix, the electrical contractor.
clean and professional looking, using company branding and colours.
I also want the blue in the logo and wording to be made a more 'electric' blue and the grey 'Voltrix' to be slightly darker.

Pleas use the following contact details:

Peter Alwick
Owner

t: 01632 960581
m: 07700 900316
e: peter@voltrix-wiring.co.uk

www.voltrix-wiring.co.uk

Industry/Entity Type

Electrical

Font styles to use
Sans Serif

```html
<!DOCTYPE html>
<html lang="en">
<head>
<meta charset="utf-8">
<title>Voltrix Business Card</title>
<link rel="stylesheet" href="https://fonts.googleapis.com/css2?family=Jura:wght@500;600&family=Quicksand:wght@500&display=swap">
<style>
  :root {
    --backdrop: #444444;
    --card-teal: #4c9aa8;
    --card-white: #ffffff;
    --text-light: #ffffff;
    --brand-grey: #5f6568;
    --electric-blue: #1a6fb8;
    --icon-dot: #ffffff;
  }
  * { margin: 0; padding: 0; box-sizing: border-box; }
  html, body {
    width: 1200px;
    height: 1000px;
    overflow: hidden;
    background: var(--backdrop);
  }
  .canvas {
    position: relative;
    width: 1200px;
    height: 1000px;
  }
  .card {
    position: absolute;
    top: 343px;
    width: 476px;
    height: 314px;
    box-shadow: 0 2px 6px rgba(0,0,0,0.35);
    overflow: hidden;
  }
  .card--front { left: 106px; background: var(--card-teal); color: var(--text-light); }
  .card--back { left: 624px; background: var(--card-white); }

  .holder { position: absolute; left: 248px; top: 28px; }
  .holder__name {
    font-family: "Jura", sans-serif;
    font-weight: 600;
    font-size: 23px;
    letter-spacing: 0.5px;
    line-height: 1;
  }
  .holder__role {
    font-family: "Quicksand", sans-serif;
    font-weight: 500;
    font-size: 12px;
    margin-top: 6px;
  }

  .contacts {
    position: absolute;
    left: 40px;
    top: 216px;
    list-style: none;
    font-family: "Quicksand", sans-serif;
    font-weight: 500;
    font-size: 13px;
  }
  .contacts__item {
    display: flex;
    align-items: center;
    height: 18px;
  }
  .contacts__icon {
    width: 13px;
    height: 13px;
    border-radius: 50%;
    background: var(--icon-dot);
    color: var(--card-teal);
    font-size: 9px;
    line-height: 13px;
    text-align: center;
    margin-right: 8px;
    font-weight: 700;
  }

  .brand {
    position: absolute;
    left: 28px;
    top: 130px;
  }
  .brand__row { display: flex; align-items: center; }
  .brand__dot {
    width: 38px;
    height: 38px;
    border-radius: 50%;
    background: var(--electric-blue);
    margin-right: 14px;
  }
  .brand__name {
    font-family: "Jura", sans-serif;
    font-weight: 600;
    font-size: 46px;
    letter-spacing: 6px;
    color: var(--brand-grey);
    line-height: 1;
  }
  .brand__tagline {
    font-family: "Jura", sans-serif;
    font-weight: 600;
    font-size: 17px;
    letter-spacing: 1.2px;
    color: var(--electric-blue);
    margin: 4px 0 0 52px;
  }
</style>
</head>
<body>
<main class="canvas">
  <section class="card card--front" aria-label="Business card front">
    <div class="holder">
      <p class="holder__name">Peter Alwick</p>
      <p class="holder__role">Owner</p>
    </div>
    <ul class="contacts">
      <li class="contacts__item"><span class="contacts__icon">m</span>07700 900316</li>
      <li class="contacts__item"><span class="contacts__icon">t</span>01632 960581</li>
      <li class="contacts__item"><span class="contacts__icon">e</span>peter@voltrix-wiring.co.uk</li>
      <li class="contacts__item"><span class="contacts__icon">w</span>www.voltrix-wiring.co.uk</li>
    </ul>
  </section>

  <section class="card card--back" aria-label="Business card back">
    <div class="brand">
      <div class="brand__row">
        <span class="brand__dot"></span>
        <span class="brand__name">VOLTRIX</span>
      </div>
      <p class="brand__tagline">THE ELECTRICAL CONTRACTOR</p>
    </div>
  </section>
</main>
</body>
</html>
```